Keystone Home Buyers website creation

A slick professional landing page it needs to be a very engaging custom designed landing page.

It must have a lead generation tool/box similar to my competitors that will recognise the address when they start to enter the address or postcode.

My main competitors websites to use ideas from to build trust and look correct are: www.brindlemarsh.com quorvahomes.com

Target Market(s)

People looking to sell their house or property fast. We will buy their property

Industry/Entity Type

Real Estate

Coding

Coded - Design and coding required

Number of Pages Required

1 page

Requirements
Must have
• A lead generation tool that is similar to my competitors to gather their essential details. (please check www.quorvahomes.com or www.brindlemarsh.com to see what i want.

It also must have all the aspects my competitors has on their landing page. All companies in this industry have this on the landing page. These include: Logos to build trust. Ours can be The Vellmoor Logo, the seen on TV logo, The Harrowgate Ledger online logo. Also we need a step by step process map to show the customer how it works.

If the customer is about to leave the page it Must have flash ups that ask the customer to fill in 4 boxes. first name, surname, email, Phone number and address. Check out quorvahomes.com to see what i want.

must have a comparison table similar to my competitors. I can include this on the draft.

Must have my frequently asked questions for google SEO ( I will upload these to here to the winner to add this page at the end.

It must be a slick professional design that tells people they are dealing with a company they can trust who has the funds on hand to purchase hundreds of property.
Nice to have
• It must be a slick professional design that tells people they are dealing with a company they can trust who has the funds on hand to purchase hundreds of property.
Should not have
• Anything cheap or tacky looking.

```html
<!DOCTYPE html>
<html lang="en">
<head>
<meta charset="utf-8">
<title>Keystone Home Buyers — We Buy Any House For Cash</title>
<link rel="stylesheet" href="https://fonts.googleapis.com/css2?family=Montserrat:wght@400;500;600;700&family=Questrial&display=swap">
<style>
:root{
  --blue:#4f86d6;
  --blue-dark:#3f74c2;
  --ink:#3b3b40;
  --muted:#6d6f75;
  --pale:#eaf0f9;
  --panel:#eeeeee;
  --footer:#56555b;
  --dark-cell:#4a4a4e;
  --white:#ffffff;
  --star:#f5a623;
}
*{box-sizing:border-box;margin:0;padding:0}
html,body{width:1200px;height:4739px;overflow:hidden}
body{position:relative;font-family:"Questrial",sans-serif;color:var(--ink);background:var(--white)}
.abs{position:absolute}
h1,h2,h3,.heading{font-family:"Montserrat",sans-serif}
.btn{position:absolute;background:var(--blue);color:var(--white);font-family:"Montserrat",sans-serif;font-weight:700;font-size:13px;letter-spacing:.5px;display:flex;align-items:center;justify-content:center;text-transform:uppercase}
.underline{position:absolute;left:560px;width:80px;height:3px;background:var(--blue)}
.brand{display:flex;align-items:center;gap:10px;font-family:"Questrial",sans-serif;font-size:17px}
.brand .mark{width:22px;height:22px;background:var(--blue)}

/* header */
.site-header{position:absolute;left:0;top:0;width:1200px;height:88px;background:var(--white)}
.site-header .brand{position:absolute;left:123px;top:30px;color:var(--ink)}
.nav{position:absolute;left:432px;top:38px;display:flex;gap:22px;font-size:12px;font-family:"Montserrat",sans-serif}
.nav a{color:var(--ink);text-decoration:none}
.nav a.active{color:var(--blue)}
.call{position:absolute;left:925px;top:26px;display:flex;gap:12px;align-items:center}
.call-box{width:36px;height:36px;border:2px solid var(--blue);border-radius:4px;display:flex;align-items:center;justify-content:center}
.call small{display:block;font-size:10px;color:var(--muted)}
.call strong{font-family:"Montserrat",sans-serif;color:var(--blue);font-size:15px;font-weight:600}

/* hero */
.hero{position:absolute;left:0;top:88px;width:1200px;height:526px;background:linear-gradient(100deg,#1f3f78 0%,#2f5592 45%,#6d7fa6 75%,#a7a4b6 100%)}
.hero h1{position:absolute;left:123px;top:95px;color:var(--white);font-size:32px;font-weight:700}
.hero .lead{position:absolute;left:123px;top:146px;width:460px;color:var(--white);font-family:"Montserrat",sans-serif;font-size:17px;line-height:28px}
.hero .find{position:absolute;left:122px;top:216px;color:var(--white);font-family:"Montserrat",sans-serif;font-size:19px;font-weight:500}
.field{position:absolute;background:var(--white);display:flex;align-items:center;gap:10px;padding-left:14px;font-size:12px;color:#9a9ca2}
.hero .reviews{position:absolute;left:124px;top:382px;color:var(--white)}
.hero .reviews b{font-family:"Montserrat",sans-serif;font-weight:500;font-size:15px;letter-spacing:.5px}
.hero .reviews span{font-size:16px;color:var(--star);margin-left:6px}
.hero .reviews p{font-size:12px;margin-top:8px}
.scroll-tab{position:absolute;left:574px;top:500px;width:52px;height:52px;border-radius:50%;background:var(--white);display:flex;justify-content:center;padding-top:14px}

/* featured */
.featured h2{position:absolute;top:688px;width:1200px;text-align:center;font-size:26px;font-weight:600;color:#45464b}
.press{position:absolute;top:754px;width:150px;height:78px;background:var(--white);box-shadow:0 2px 10px rgba(0,0,0,.08);display:flex;align-items:center;justify-content:center;font-family:"Questrial",sans-serif;font-size:18px;color:#55565b}
.press .badge{width:52px;height:44px;background:#e0424b;border-radius:4px}
.arrow-s{position:absolute;top:782px;font-size:22px;color:#999}

/* how it works */
.how{position:absolute;left:0;top:916px;width:1200px;height:450px;background:var(--panel)}
.how-photo{position:absolute;left:0;top:0;width:520px;height:450px;background:linear-gradient(160deg,#9a7a5a 0%,#b79a72 35%,#6f8a52 70%,#c9b28a 100%);clip-path:polygon(0 0,515px 0,410px 225px,515px 450px,0 450px)}
.how h2{position:absolute;left:560px;top:50px;font-size:30px;font-weight:600;color:#4a4b50}
.step{position:absolute;top:122px;width:170px}
.step .ring{width:90px;height:90px;border-radius:50%;background:var(--blue);display:flex;align-items:center;justify-content:center;box-shadow:0 0 0 5px rgba(79,134,214,.25)}
.step p{font-size:12px;line-height:18px;margin-top:14px;color:#555}
.step-arrow{position:absolute;top:148px;color:var(--blue);font-size:28px;font-family:"Montserrat",sans-serif}
.how h3{position:absolute;left:560px;top:300px;font-size:22px;font-weight:700;color:#3b3b40}

/* why */
.why h2{position:absolute;top:1484px;width:1200px;text-align:center;font-size:28px;font-weight:600;color:#45464b}
.stat{position:absolute;top:1568px;width:220px;text-align:center}
.stat .ic{width:76px;height:76px;border-radius:50%;background:var(--pale);margin:0 auto;display:flex;align-items:center;justify-content:center}
.stat b{display:block;font-family:"Montserrat",sans-serif;font-size:23px;font-weight:500;margin-top:16px}
.stat p{font-size:12px;line-height:20px;margin-top:8px;color:#444}
.stat-sep{position:absolute;top:1575px;width:1px;height:150px;background:#e2e2e2}

/* customer reviews */
.testimonials{position:absolute;left:0;top:1884px;width:1200px;height:696px;background:linear-gradient(120deg,#1d3244 0%,#2e4a5c 40%,#5b5a52 70%,#2d3b47 100%)}
.testimonials::after{content:"";position:absolute;inset:0;background:rgba(20,40,60,.35)}
.testimonials>*{position:absolute;z-index:1}
.testimonials h2{top:72px;width:1200px;text-align:center;color:var(--white);font-size:30px;font-weight:700}
.testimonials .intro{top:142px;left:260px;width:680px;text-align:center;color:var(--white);font-size:12px;line-height:20px}
.review{top:252px;width:307px;height:201px;background:rgba(255,255,255,.93);text-align:center;padding-top:56px}
.review.focus{background:var(--white)}
.review .face{position:absolute;left:113px;top:-40px;width:80px;height:80px;border-radius:50%;background:linear-gradient(#c9d6e4,#8ea3b8);border:3px solid var(--white)}
.review h4{font-family:"Questrial",sans-serif;font-weight:400;font-size:15px;color:#333}
.review small{display:block;font-size:12px;color:#9a9ca2;margin-top:6px}
.review p{font-size:11.5px;font-style:italic;color:#555;line-height:20px;margin:14px 24px 0}
.dots{top:491px;left:563px;display:flex;gap:5px}
.dots i{width:10px;height:10px;border-radius:50%;border:1px solid var(--white);display:block}
.dots i.on{background:var(--blue);border-color:var(--blue)}
.rating{top:538px;width:1200px;text-align:center;color:var(--white)}
.rating .stars{font-size:38px;color:var(--star);letter-spacing:4px}
.rating p{font-family:"Montserrat",sans-serif;font-size:30px;margin-top:2px}

/* comparison */
.compare h2{position:absolute;top:2650px;width:1200px;text-align:center;font-size:30px;font-weight:600;color:#45464b}
.table{position:absolute;left:160px;top:2736px;width:878px;border-collapse:collapse;font-size:13px}
.table td,.table th{padding:0 30px;height:45px;font-weight:400}
.table td.num,.table th.num{text-align:center;padding:0;width:179px}
.table tr.alt td{background:var(--pale)}
.table .head-title{background:var(--blue);color:var(--white);vertical-align:bottom;padding-bottom:14px;font-family:"Montserrat",sans-serif;font-weight:700;font-size:19px}
.table .head-title .mark{display:block;width:26px;height:26px;background:rgba(255,255,255,.9);margin-bottom:12px}
.table .col-label{background:#b8cdeb;color:#3b3b40;height:44px;font-size:13px}
.table .col-value{background:var(--blue);color:var(--white);font-family:"Montserrat",sans-serif;font-size:21px;font-weight:700;height:46px}
.table tr.tall td{height:76px;line-height:20px}
.table .final-label td.num{background:var(--blue);color:var(--white);height:42px}
.table .final-value td.num{background:var(--dark-cell);color:var(--white);font-family:"Montserrat",sans-serif;font-size:22px;font-weight:600;height:44px}
.table tr.final-label td.blank,.table tr.final-value td.blank{background:transparent}

/* cta banner */
.cta{position:absolute;left:0;top:3373px;width:1200px;height:291px;background:linear-gradient(180deg,#3a3c42 0%,#5a5b5f 50%,#3d3e44 100%)}
.cta h2{position:absolute;top:80px;width:1200px;text-align:center;color:var(--white);font-size:31px;font-weight:700;line-height:44px}

/* faq */
.footer-band{position:absolute;left:0;top:4173px;width:1200px;height:566px;background:var(--footer)}
.faq{position:absolute;left:160px;top:3741px;width:878px;height:620px;background:var(--white);box-shadow:0 4px 24px rgba(0,0,0,.12)}
.faq h2{position:absolute;top:74px;width:878px;text-align:center;font-size:30px;font-weight:600;color:#45464b}
.q{position:absolute;left:90px;width:735px;height:32px;background:var(--pale);display:flex;align-items:center;justify-content:space-between;padding:0 14px;font-size:12px;color:#333}
.q .plus{width:18px;height:18px;border-radius:50%;background:var(--blue);color:var(--white);font-size:14px;line-height:18px;text-align:center}
.q.open{background:var(--blue);color:var(--white)}
.q.open .plus{background:var(--white);color:var(--blue)}
.answer{position:absolute;left:90px;top:192px;width:735px;height:96px;background:var(--white);box-shadow:0 2px 8px rgba(0,0,0,.08);padding:22px 14px;font-size:12px;line-height:25px;color:#444}

/* footer */
.site-footer{position:absolute;left:0;top:4173px;width:1200px;height:566px;color:var(--white)}
.site-footer .brand{position:absolute;left:123px;top:256px;color:var(--white)}
.site-footer .about{position:absolute;left:124px;top:336px;width:210px;font-size:12px;line-height:17px}
.site-footer h5{position:absolute;font-family:"Montserrat",sans-serif;font-weight:600;font-size:14px}
.links{position:absolute;left:353px;top:292px;display:grid;grid-template-columns:130px 130px;row-gap:12px;font-size:11px}
.contact{position:absolute;display:flex;gap:14px;font-size:11px;line-height:19px}
.contact .ci{width:38px;height:38px;border:2px solid var(--white);border-radius:50%;display:flex;align-items:center;justify-content:center;flex:none}
.privacy{position:absolute;left:353px;top:404px;width:720px;font-size:11px;line-height:18px}
.copyright{position:absolute;top:526px;width:1200px;text-align:center;font-size:12px}
</style>
</head>
<body>

<header class="site-header">
  <div class="brand"><span class="mark"></span>Keystone Home Buyers</div>
  <nav class="nav">
    <a class="active" href="#">Home</a><a href="#">How it Works</a><a href="#">Sell Property Fast</a><a href="#">Value My House</a><a href="#">About Us</a>
  </nav>
  <div class="call">
    <div class="call-box"><svg width="18" height="18" viewBox="0 0 24 24"><path d="M6.6 10.8a15 15 0 006.6 6.6l2.2-2.2c.3-.3.7-.4 1-.2 1.1.4 2.3.6 3.6.6.6 0 1 .4 1 1V20c0 .6-.4 1-1 1A17 17 0 013 4c0-.6.4-1 1-1h3.5c.6 0 1 .4 1 1 0 1.3.2 2.5.6 3.6.1.3 0 .7-.2 1z" fill="#4f86d6"/></svg></div>
    <div><small>Call Us Today</small><strong>123 456 7890</strong></div>
  </div>
</header>

<section class="hero">
  <div role="img" aria-label="Photo of a large detached family house with a double garage at dusk" class="abs" style="inset:0"></div>
  <h1>We Buy Any House For Cash</h1>
  <p class="lead">We Can Buy Your Property For Cash Have Your Money In As Little As Two Weeks</p>
  <p class="find">Find Out How Much You Can Get</p>
  <div class="field" style="left:123px;top:259px;width:414px;height:46px">
    <svg width="14" height="18" viewBox="0 0 14 18"><path d="M7 0a7 7 0 017 7c0 5-7 11-7 11S0 12 0 7a7 7 0 017-7z" fill="#4f86d6"/><circle cx="7" cy="7" r="2.5" fill="#fff"/></svg>Enter Your Postcode</div>
  <div class="btn" style="left:123px;top:323px;width:137px;height:41px">Get An Offer</div>
  <div class="reviews"><b>REVIEWS</b><span>★★★★★</span><p>4.89 Average | 531 Reviews</p></div>
  <div class="scroll-tab"><svg width="14" height="9" viewBox="0 0 14 9"><path d="M1 1l6 6 6-6" stroke="#4f86d6" stroke-width="2" fill="none"/></svg></div>
</section>

<section class="featured">
  <h2>As Featured On</h2>
  <span class="arrow-s" style="left:138px">‹</span>
  <div class="press" style="left:160px">Harbourline</div>
  <div class="press" style="left:342px">The Vellmoor</div>
  <div class="press" style="left:523px"><span class="badge"></span></div>
  <div class="press" style="left:705px">Cityway</div>
  <div class="press" style="left:887px">Northcast</div>
  <span class="arrow-s" style="left:1053px">›</span>
</section>

<section class="how">
  <div class="how-photo" role="img" aria-label="Photo of a white clapboard house with red windows behind a picket fence in autumn"></div>
  <h2>How It Works</h2>
  <div class="step" style="left:558px">
    <div class="ring"><svg width="34" height="40" viewBox="0 0 34 40"><rect x="3" y="2" width="26" height="34" rx="2" fill="none" stroke="#fff" stroke-width="2.5"/><path d="M9 12h14M9 18h14M9 24h9" stroke="#fff" stroke-width="2.5"/></svg></div>
    <p>Request Your<br>Free Valuation</p>
  </div>
  <span class="step-arrow" style="left:683px">›</span>
  <div class="step" style="left:740px">
    <div class="ring"><svg width="40" height="40" viewBox="0 0 40 40"><circle cx="20" cy="20" r="15" fill="none" stroke="#fff" stroke-width="2.5"/><path d="M20 10v10l6 4" stroke="#fff" stroke-width="2.5" fill="none"/></svg></div>
    <p>Receive Your Cash<br>Offer In 1 Hour</p>
  </div>
  <span class="step-arrow" style="left:865px">›</span>
  <div class="step" style="left:921px">
    <div class="ring"><svg width="42" height="34" viewBox="0 0 42 34"><path d="M3 14l10-8 8 5 8-5 10 8-10 12-8-6-8 6z" fill="none" stroke="#fff" stroke-width="2.5" stroke-linejoin="round"/></svg></div>
    <p>Once Agreed Your Cash<br>Sale Is Guaranteed</p>
  </div>
  <h3>Start With A Free Cash Offer...</h3>
  <div class="field" style="left:560px;top:347px;width:263px;height:45px;border:1px solid #dcdcdc">
    <svg width="11" height="14" viewBox="0 0 14 18"><path d="M7 0a7 7 0 017 7c0 5-7 11-7 11S0 12 0 7a7 7 0 017-7z" fill="#9a9ca2"/></svg>Enter your Address or postcode</div>
  <div class="btn" style="left:823px;top:347px;width:152px;height:45px">Get An Offer</div>
</section>

<section class="why">
  <h2>Why Choose House Buying?</h2>
  <div class="underline" style="top:1535px"></div>
  <div class="stat" style="left:126px"><div class="ic"><svg width="34" height="32" viewBox="0 0 34 32"><rect x="2" y="5" width="30" height="25" rx="2" fill="none" stroke="#444" stroke-width="2"/><path d="M2 12h30M9 2v6M25 2v6" stroke="#444" stroke-width="2"/></svg></div><b>1993</b><p>Operating Since 1993</p></div>
  <div class="stat-sep" style="left:358px"></div>
  <div class="stat" style="left:370px"><div class="ic"><svg width="34" height="32" viewBox="0 0 34 32"><path d="M3 15L17 3l14 12M7 12v17h20V12" fill="none" stroke="#444" stroke-width="2"/><rect x="14" y="19" width="6" height="10" fill="#444"/></svg></div><b>6,000</b><p>We Have Bought More Than<br>6,000 Properties</p></div>
  <div class="stat-sep" style="left:602px"></div>
  <div class="stat" style="left:615px"><div class="ic"><svg width="34" height="34" viewBox="0 0 34 34"><circle cx="17" cy="17" r="14" fill="none" stroke="#444" stroke-width="2"/><path d="M17 8v9l6 4" stroke="#444" stroke-width="2" fill="none"/></svg></div><b>Timescales</b><p>You Are In Complete<br>Control</p></div>
  <div class="stat-sep" style="left:847px"></div>
  <div class="stat" style="left:860px"><div class="ic"><svg width="34" height="34" viewBox="0 0 34 34"><circle cx="17" cy="17" r="14" fill="none" stroke="#444" stroke-width="2"/><path d="M21 11a4 4 0 00-7 2v11M11 18h8M11 24h12" stroke="#444" stroke-width="2" fill="none"/></svg></div><b>£34.2 m</b><p>Our Current Annual<br>Turnover</p></div>
  <div class="btn" style="left:531px;top:1769px;width:137px;height:41px">Get An Offer</div>
</section>

<section class="testimonials" role="img" aria-label="Photo of friends gathered around a table in a living room">
  <h2>Customer Reviews</h2>
  <p class="intro">Lorem ipsum dolor sit amet, consectetuer adipiscing elit, sed diam nonummy nibh euismod tincidunt ut laoreet dolore magna aliquam erat volutpat. Ut wisi enim ad minim veniam quis nostrud exerci.</p>
  <div class="review" style="left:131px"><span class="face" role="img" aria-label="Customer portrait"></span><h4>Mr Lorems</h4><small>Lorem Ipsum</small><p>" Lorem ipsum dolor sit amet, consectetuer adipiscing elit, sed diam nonummy nibh euismod tincidunt nonummy "</p></div>
  <div class="review focus" style="left:449px"><span class="face" role="img" aria-label="Customer portrait"></span><h4>Ms Clara Venn</h4><small>Lorem Ipsum</small><p>" Lorem ipsum dolor sit amet, consectetuer adipiscing elit, sed diam nonummy nibh euismod tincidunt nonummy "</p></div>
  <div class="review" style="left:769px"><span class="face" role="img" aria-label="Customer portrait"></span><h4>Mr Legister</h4><small>Lorem Ipsum</small><p>" Lorem ipsum dolor sit amet, consectetuer adipiscing elit, sed diam nonummy nibh euismod tincidunt nonummy "</p></div>
  <div class="dots"><i></i><i></i><i class="on"></i><i></i><i></i></div>
  <div class="rating"><div class="stars">★★★★★</div><p>4.89 out of 5</p></div>
</section>

<section class="compare">
  <h2>Comparison Table</h2>
  <div class="underline" style="top:2703px"></div>
  <table class="table">
    <tr>
      <th class="head-title" rowspan="2" style="text-align:left"><span class="mark"></span>Sale Process</th>
      <th class="num col-label">Estate Agent</th><th class="num col-label">Our Service</th>
    </tr>
    <tr><th class="num col-value">9 Months</th><th class="num col-value">7 Days</th></tr>
    <tr><td>Market value (Advertised Price)</td><td class="num">£100,000</td><td class="num">£80,000</td></tr>
    <tr class="alt"><td>Offer Accepted (Typical 5% Discount)</td><td class="num">£95,000</td><td class="num">£80,000</td></tr>
    <tr><td>Post survey negotiation</td><td class="num">£92,500</td><td class="num">£80,000</td></tr>
    <tr class="alt"><td>Estate agent (£92,500 @ 2% + VAT)</td><td class="num">£90,280</td><td class="num">£80,000</td></tr>
    <tr><td>Solicitor Fees (£1000 + VAT = £1200)</td><td class="num">£89,080</td><td class="num">£80,000</td></tr>
    <tr class="alt tall"><td>Mortgage payments (£75K repayment @ 5%<br>PA = £563pcm or £5067 for 9 Months)</td><td class="num">£84,017</td><td class="num">£80,000</td></tr>
    <tr><td>Utility bills and Council Tax (£375 x 9 months)</td><td class="num">£80,642</td><td class="num">£80,000</td></tr>
    <tr class="alt"><td>Property Clearance (Skip &amp; Deep Clean @£750)</td><td class="num">£79,892</td><td class="num">£80,000</td></tr>
    <tr class="final-label"><td class="blank"></td><td class="num">Final Price</td><td class="num">Final Price</td></tr>
    <tr class="final-value"><td class="blank"></td><td class="num">£79,892</td><td class="num">£80,000</td></tr>
  </table>
</section>

<section class="cta" role="img" aria-label="Photo of a brick house frontage with garage doors">
  <h2>Fill In The Form And Within 15 Seconds You Will<br>Be Pleasantly Surprised With Our Cash Offer</h2>
  <div class="btn" style="left:531px;top:180px;width:137px;height:38px">Get An Offer</div>
</section>

<div class="footer-band"></div>

<section class="faq">
  <h2>Frequently Asked Questions</h2>
  <div class="q open" style="top:160px">How much will you offer me?<span class="plus">−</span></div>
  <div class="answer">Lorem ipsum dolor sit amet, consectetuer adipiscing elit, sed diam nonummy nibh euismod tincidunt ut laoreet dolore magna aliquam erat volutpat. Ut wisi enim ad minim veniam.</div>
  <div class="q" style="top:303px">Does anybody have to know about this sale?<span class="plus">+</span></div>
  <div class="q" style="top:351px">Do I need to complete lots of paperwork?<span class="plus">+</span></div>
  <div class="q" style="top:399px">Do I need to complete lots of paperwork?<span class="plus">+</span></div>
  <div class="q" style="top:447px">What if I don't want to proceed?<span class="plus">+</span></div>
  <div class="q" style="top:495px">What if I don't want to move out quickly?<span class="plus">+</span></div>
</section>

<footer class="site-footer">
  <div class="brand"><span class="mark" style="background:#fff"></span>Keystone Home Buyers</div>
  <p class="about">KEYSTONE HOME BUYERS ESTATE is the UK's No. 1 Property Buyer since 1993</p>
  <h5 style="left:353px;top:250px">Useful Links</h5>
  <div class="links"><span>• Home</span><span>• Value My House</span><span>• How it Works</span><span>• About Us</span><span>• Sell Property Fast</span><span>• Contact Us</span></div>
  <h5 style="left:610px;top:250px">Contact Details</h5>
  <div class="contact" style="left:610px;top:288px">
    <span class="ci"><svg width="14" height="18" viewBox="0 0 14 18"><path d="M7 1a6 6 0 016 6c0 4.5-6 10-6 10S1 11.5 1 7a6 6 0 016-6z" fill="none" stroke="#fff" stroke-width="1.6"/><circle cx="7" cy="7" r="2" fill="#fff"/></svg></span>
    <div><b>KEYSTONE HOMES</b><br>123/33 building Name, Street<br>Name, City Name, State Name<br>XY 123456, UK</div>
  </div>
  <div class="contact" style="left:880px;top:288px">
    <span class="ci"><svg width="16" height="16" viewBox="0 0 24 24"><path d="M6.6 10.8a15 15 0 006.6 6.6l2.2-2.2c.3-.3.7-.4 1-.2 1.1.4 2.3.6 3.6.6.6 0 1 .4 1 1V20c0 .6-.4 1-1 1A17 17 0 013 4c0-.6.4-1 1-1h3.5c.6 0 1 .4 1 1 0 1.3.2 2.5.6 3.6.1.3 0 .7-.2 1z" fill="#fff"/></svg></span>
    <div><b>Call Us Today</b><br><span style="font-size:13px">123 456 7890</span><br>7 Days a Week (8am-8pm)</div>
  </div>
  <p class="privacy"><b>Privacy Policy:</b> Lorem ipsum dolor sit amet, consectetuer adipiscing elit, sed diam nonummy nibh euismod tincidunt ut laoreet dolore magna aliquam erat volutpat. Ut wisi enim ad minim veniam, quis nostrud exerci tation.</p>
  <p class="copyright">Copyright © 2020 <b>Keystone Home Buyers</b>. All Rights Reserved.</p>
</footer>

</body>
</html>
```